Film and TV production company

I have the logo already designed by mark quarry. I just need the text and the logo attached to the business card. Maybe a small design on the back of the card or text.

Industry/Entity Type

film tv arts

Contact Information for Business Card

Dale Morrow Cinematographer-Director

Colors
F0912C
F2A743
F7CA91
FBE8D2
FDF5EE
EE7325
F08F49
F5BC92
FAE3D3
FDF4ED

Requirements
Must have
• www.copperlanepix.com.au my email address mail@copperlanepix.com.au my mobile number 0491570158
Nice to have
• Some kind of small art work on the back that ties in with the logo design attached
Should not have
• Must clean and simple

```html
<!DOCTYPE html>
<html lang="en">
<head>
<meta charset="utf-8">
<title>Copper Lane Pix — Business Card</title>
<link rel="stylesheet" href="https://fonts.googleapis.com/css2?family=Raleway:wght@400;500&family=Ubuntu:wght@300;400;500&display=swap">
<style>
  :root {
    --backdrop: #1f1f1f;
    --copper: #c96c3c;
    --amber: #e0973a;
    --gold: #ebae34;
    --sun-orange: #e47c14;
    --light-glow: #f7ca91;
    --paper: #fbfaf8;
    --paper-shade: #d9d9d9;
    --ink: #111111;
    --white: #ffffff;
    --rule-grey: #cfcfcf;
  }
  * { box-sizing: border-box; margin: 0; padding: 0; }
  html, body { width: 1200px; height: 888px; overflow: hidden; }
  body { background: var(--backdrop); position: relative; font-family: "Ubuntu", sans-serif; }

  .card { position: absolute; width: 525px; height: 352px; overflow: hidden; }

  /* Contact side */
  .card--contact {
    left: 45px; top: 110px;
    background:
      radial-gradient(ellipse 320px 200px at 100% 100%, var(--light-glow) 0%, rgba(247,202,145,0) 75%),
      linear-gradient(90deg, var(--copper) 0%, var(--copper) 30%, var(--amber) 65%, var(--gold) 100%);
    color: var(--white);
  }
  .brand-block { position: absolute; left: 40px; top: 26px; width: 170px; text-align: center; }
  .brand-dot { width: 74px; height: 74px; border-radius: 50%; background: var(--sun-orange); margin: 0 auto 12px; }
  .brand-name { font-family: "Raleway", sans-serif; font-weight: 500; font-size: 18px; letter-spacing: 3.5px; white-space: nowrap; }
  .brand-country { font-family: "Raleway", sans-serif; font-weight: 500; font-size: 7px; letter-spacing: 4px; margin-top: 2px; }

  .contact-row { position: absolute; left: 26px; padding-left: 18px; border-left: 5px solid var(--white); }
  .contact-row--person { top: 176px; height: 36px; }
  .contact-row--phone { top: 236px; height: 36px; padding-top: 8px; }
  .contact-row--web { top: 296px; height: 38px; }
  .person-name { font-weight: 500; font-size: 16px; line-height: 16px; }
  .person-role { font-weight: 300; font-size: 16px; line-height: 18px; }
  .phone { font-weight: 300; font-size: 17px; letter-spacing: 0.5px; }
  .web-line { font-weight: 300; font-size: 15px; line-height: 15px; }

  /* Brand side */
  .card--brand {
    left: 630px; top: 426px;
    background:
      radial-gradient(ellipse 420px 200px at 100% 100%, var(--paper-shade) 0%, rgba(217,217,217,0) 80%),
      var(--paper);
    color: var(--ink);
  }
  .brand-side-dot { position: absolute; left: 189px; top: 80px; width: 147px; height: 147px; border-radius: 50%; background: var(--sun-orange); }
  .brand-side-rule { position: absolute; left: 0; right: 0; top: 240px; height: 1px; background: var(--rule-grey); }
  .brand-side-name { position: absolute; left: 0; right: 0; top: 241px; text-align: center; font-family: "Raleway", sans-serif; font-weight: 500; font-size: 36px; letter-spacing: 8px; padding-left: 8px; white-space: nowrap; }
  .brand-side-country { position: absolute; left: 0; right: 0; top: 293px; text-align: center; font-family: "Raleway", sans-serif; font-weight: 500; font-size: 13px; letter-spacing: 9px; padding-left: 9px; }
</style>
</head>
<body>
  <section class="card card--contact" aria-label="Contact side of business card">
    <div class="brand-block">
      <div class="brand-dot"></div>
      <div class="brand-name">COPPER LANE PIX</div>
      <div class="brand-country">AUSTRALIA</div>
    </div>

    <div class="contact-row contact-row--person">
      <div class="person-name">Dale Morrow</div>
      <div class="person-role">Cinematographer - Director</div>
    </div>
    <div class="contact-row contact-row--phone">
      <div class="phone">0491570158</div>
    </div>
    <div class="contact-row contact-row--web">
      <div class="web-line">www.copperlanepix.com.au</div>
      <div class="web-line">mail@copperlanepix.com.au</div>
    </div>
  </section>

  <section class="card card--brand" aria-label="Brand side of business card">
    <div class="brand-side-dot"></div>
    <div class="brand-side-rule"></div>
    <div class="brand-side-name">COPPER LANE PIX</div>
    <div class="brand-side-country">AUSTRALIA</div>
  </section>
</body>
</html>
```